Clear Plastic Card Design

I am looking to have a business card designed from my logo icon. I am looking to match the style of a different business card I have attached in the files.
Looking for a card that is plastic, with layers of transparency in the shape of my logo icon (also attached in the files) - not a circle like the other card. The winning design will incorporate the red icon logo on the front and back and include the charity's name, "Lanterns for the Weary" in the same or similar font, as well as an email and phone number. For now, use the email: email@lanternsfortheweary.org and the phone number 555-318-4072.
We like how the sample business card has transparency, partial and full opacity layers and a matching color scheme. Files will need to be in vector so that our business card printing company can work with it.
UPDATE:
We've some excellent designs in, thank you everyone! I got an early review from the owner, and he requested a minor redirect to find his perfect design. He wants the design to stand out by NOT being a rectangle. Try instead a circle, square, or best yet - something that falls in the outline of the logo icon, either fully or partially. Thank you, everyone!
Contact Information for Business Card
Lanterns for the Weary text should be incorporated as well as a phone and email.
Look and feel

```html
<!DOCTYPE html>
<html lang="en">
<head>
<meta charset="utf-8">
<title>Lanterns for the Weary – Business Cards</title>
<link rel="stylesheet" href="https://fonts.googleapis.com/css2?family=Bebas+Neue&family=Questrial&display=swap">
<style>
  :root {
    --stage: #2b2b2b;
    --card-red: #8e0c05;
    --card-red-deep: #6f0903;
    --card-white: #f4f4f4;
    --brand-orange: #ef5a12;
    --brand-red: #d8200f;
    --ink-white: #ffffff;
    --ink-dark: #222222;
  }
  * { box-sizing: border-box; margin: 0; padding: 0; }
  html, body { width: 1200px; height: 800px; overflow: hidden; background: var(--stage); }
  .canvas { position: relative; width: 1200px; height: 800px; }

  .card {
    position: absolute;
    left: 380px;
    width: 520px;
    height: 310px;
    border-radius: 4px;
  }
  .card--front { top: 60px; background: linear-gradient(135deg, var(--card-red) 0%, var(--card-red-deep) 100%); }
  .card--back  { top: 430px; background: var(--card-white); }

  .brand-mark {
    position: absolute;
    left: -90px;
    top: 70px;
    display: flex;
    align-items: center;
    gap: 12px;
    font-family: "Bebas Neue", sans-serif;
    font-size: 52px;
    line-height: 0.9;
    color: var(--brand-orange);
    width: 260px;
  }
  .brand-mark__square { flex: none; width: 22px; height: 22px; background: var(--brand-red); }

  .front-title {
    position: absolute;
    right: 36px;
    top: 48px;
    font-family: "Bebas Neue", sans-serif;
    color: var(--ink-white);
    text-align: left;
    line-height: 0.9;
  }
  .front-title__line1 { font-size: 66px; display: block; }
  .front-title__line2 { font-size: 46px; display: block; }

  .contact {
    position: absolute;
    right: 36px;
    font-family: "Bebas Neue", sans-serif;
    color: var(--ink-white);
    display: flex;
    align-items: center;
    gap: 8px;
  }
  .contact--phone { top: 190px; font-size: 32px; }
  .contact--email { top: 250px; font-size: 22px; letter-spacing: 0.3px; }
  .contact svg { fill: var(--brand-orange); flex: none; }

  .back-lockup {
    position: absolute;
    right: 40px;
    bottom: 60px;
    text-align: right;
  }
  .back-lockup__mark {
    display: inline-flex;
    align-items: center;
    gap: 8px;
    font-family: "Questrial", sans-serif;
    font-size: 18px;
    color: var(--brand-red);
    margin-bottom: 10px;
  }
  .back-lockup__mark span.square { width: 12px; height: 12px; background: var(--brand-red); display: inline-block; }
  .back-lockup__name {
    font-family: "Questrial", sans-serif;
    color: var(--ink-dark);
    font-size: 28px;
    line-height: 1.05;
  }
</style>
</head>
<body>
<main class="canvas">

  <section class="card card--front" aria-label="Front of card">
    <div class="brand-mark"><span class="brand-mark__square"></span><span>Lanterns for the Weary</span></div>
    <h1 class="front-title">
      <span class="front-title__line1">LANTERNS FOR</span>
      <span class="front-title__line2">THE WEARY</span>
    </h1>
    <p class="contact contact--phone">
      <svg width="24" height="24" viewBox="0 0 24 24" aria-hidden="true"><path d="M6.6 10.8a15.1 15.1 0 0 0 6.6 6.6l2.2-2.2a1 1 0 0 1 1-.25 11.4 11.4 0 0 0 3.6.57 1 1 0 0 1 1 1V20a1 1 0 0 1-1 1A17 17 0 0 1 3 4a1 1 0 0 1 1-1h3.5a1 1 0 0 1 1 1c0 1.25.2 2.45.57 3.57a1 1 0 0 1-.25 1z"/></svg>
      555-318-4072
    </p>
    <p class="contact contact--email">
      <svg width="18" height="18" viewBox="0 0 24 24" aria-hidden="true"><path d="M2 12 22 2 16 22l-4-8z"/></svg>
      EMAIL@LANTERNSFORTHEWEARY.ORG
    </p>
  </section>

  <section class="card card--back" aria-label="Back of card">
    <div class="brand-mark"><span class="brand-mark__square"></span><span>Lanterns for the Weary</span></div>
    <div class="back-lockup">
      <div class="back-lockup__mark"><span class="square"></span>Lanterns for the Weary</div>
      <p class="back-lockup__name">Lanterns for the<br>Weary</p>
    </div>
  </section>

</main>
</body>
</html>
```